Web Design Project for Sports Bar

We are redesigning a new clients webpage. Old site is VERY antiquated. The client is a sports bar in the Seattle Area.

Bar's name: The Copper Lantern

This sports bar has pool tables, darts, poker, dancing with a DJ every Wed-Saturday.
They have area for watching major sporting events. KTB, PWJ, QDR, VGT, JXP, etc...

Every holiday they typically host events for their patrons.

This could be a combo job. They have 2 bar's with slightly different genre. We are redesigning both sites.

We want to have Trelvio plugin integrated and other social media references, (i.e. Quib)

We have guaranteed the funds for this site.  We also have another that is similar that we will be posting again for a sister bar.  This could be a 2 for one deal.  Our client is anxiously looking for some examples.  Please post your designs if you are close.  

Reason: client was out of town is now just reviewing designs. hopefully will have some meaningful feedback soon.

Target Market(s)

Age 21-50, Sports enthusiasts, dancers, "hiphopsters"

Industry/Entity Type

Sports Bar

Requirements
Must have
• Navigation will be:

Home
Menus
Events
KTB
PWJ
Poker
Entertainment
Karaoke
DJ Dancing
Group Parties
Location/Directions
Contact

```html
<!DOCTYPE html>
<html lang="en">
<head>
<meta charset="utf-8">
<title>The Copper Lantern – Sports Bar</title>
<link href="https://fonts.googleapis.com/css2?family=Oswald:wght@400;600;700&family=Pacifico&family=Great+Vibes&family=Roboto+Slab:wght@400;700&family=Arimo&family=Open+Sans:wght@600;700&display=swap" rel="stylesheet">
<style>
:root{
  --page:#121212;
  --panel:#1b1b1b;
  --panel-edge:#262626;
  --orange:#ff7a00;
  --orange-deep:#e35f00;
  --text-grey:#a9a9a9;
  --muted:#8c8c8c;
  --white:#ffffff;
  --nav-ink:#2a1200;
  --social:#cfcfcf;
  --fb-blue:#3b5998;
  --fb-link:#3b6fb8;
  --fb-green:#5fa73a;
}
*{box-sizing:border-box;margin:0;padding:0}
html,body{width:1068px;height:1200px;overflow:hidden;background:var(--page)}
.canvas{position:relative;width:1068px;height:1200px;overflow:hidden;
  background:radial-gradient(ellipse at 50% 20%,#232323 0%,#151515 55%,#0d0d0d 100%);
  font-family:"Arimo",Arial,sans-serif}
.abs{position:absolute}

/* header */
.brand{left:164px;top:14px;display:flex;align-items:center;gap:12px}
.brand-mark{width:78px;height:78px;border-radius:50%;background:#8d8d8d}
.brand-name{font-family:"Oswald",sans-serif;font-weight:700;font-size:30px;color:var(--orange);line-height:1}
.follow{left:854px;top:6px;font-family:"Oswald",sans-serif;font-weight:600;font-size:13px;color:#9a9a9a}
.social{top:29px;width:25px;height:25px;border-radius:4px;background:var(--social)}
.phone-ring{left:740px;top:60px;width:37px;height:37px;border:2px solid #6b6b6b;border-radius:50%}
.phone-number{left:785px;top:60px;font-family:"Oswald",sans-serif;font-weight:600;font-size:27px;letter-spacing:1px;color:#8a8a8a}

/* nav band */
.band{left:0;top:104px}
.nav{left:0;top:127px;width:1068px;height:25px}
.nav a{position:absolute;top:0;height:25px;line-height:25px;transform:translateX(-50%);
  font-family:"Oswald",sans-serif;font-weight:600;font-size:11px;color:var(--nav-ink);text-decoration:none;white-space:nowrap}
.nav a.current{background:#1e1e1e;color:var(--white);border-radius:5px;width:62px;text-align:center;box-shadow:0 0 0 1px #555}

/* main panel */
.panel{left:123px;top:164px;width:822px;height:961px;background:linear-gradient(#1d1d1d,#171717)}
.slider-frame{left:148px;top:230px;width:768px;height:327px;border-radius:10px;background:linear-gradient(#333,#141414);border:1px solid #4a4a4a}
.slide{left:168px;top:245px;width:729px;height:296px;
  background:radial-gradient(ellipse at 65% 35%,#f0b07a 0%,transparent 35%),linear-gradient(#d8502a 0%,#a3502f 35%,#6a3a22 70%,#4c3a4a 100%)}
.headline{left:176px;top:160px;width:700px;text-align:center;font-family:"Pacifico",cursive;font-size:50px;color:var(--white);
  text-shadow:3px 3px 0 var(--orange),-2px -2px 0 var(--orange),2px -2px 0 var(--orange),-2px 2px 0 var(--orange)}
.dots{left:460px;top:516px;width:158px;height:49px;border-radius:25px;background:linear-gradient(#555,#2a2a2a);display:flex;justify-content:center;align-items:center;gap:7px}
.dots span{width:18px;height:18px;border-radius:50%;background:radial-gradient(#9a9a9a,#5a5a5a);border:2px solid #3a3a3a}

.leagues{left:136px;top:575px;width:792px;height:95px;background:#0b0b0b}
.league{position:absolute;top:12px;height:70px;display:flex;align-items:center;gap:7px;
  font-family:"Oswald",sans-serif;font-weight:700;font-size:30px;color:var(--white)}
.league i{display:block;width:16px;height:16px}

/* sidebar */
.sidebar{left:133px;top:680px;width:147px;height:385px;border:1px solid #333;background:#161616}
.tap{position:absolute;left:19px;width:104px;height:78px;background:linear-gradient(#6a6a6a,#4a4a4a);display:flex;align-items:center;justify-content:center}
.tap span{display:flex;align-items:center;justify-content:center;width:88px;height:48px;border-radius:50%;background:#0c0c0c;
  font-family:"Oswald",sans-serif;font-weight:400;font-size:13px;color:var(--white)}

/* welcome */
.welcome-title{left:315px;top:676px;font-family:"Great Vibes",cursive;font-size:44px;color:#9a9a9a}
.welcome-rule{left:315px;top:734px;width:371px;border-top:1px dotted #3c3c3c}
.welcome-copy{left:314px;top:744px;width:370px;font-size:9.6px;line-height:14.8px;color:var(--text-grey);text-align:justify;letter-spacing:.2px}

.feature{left:306px;top:880px;width:387px;height:233px;border-radius:10px;background:#0d0d0d;border:1px solid #2e2e2e}
.feature-title{left:306px;top:886px;width:387px;text-align:center;font-family:"Roboto Slab",serif;font-weight:700;font-size:20px;color:var(--white)}
.poster{left:322px;top:918px;width:354px;height:179px;background:linear-gradient(90deg,#8a7a70 0%,#3b3a3d 30%,#2d5c7a 50%,#3b3a3d 70%,#8a7a70 100%)}
.poster-text{left:322px;top:918px;width:354px;height:179px;text-align:center;font-family:"Oswald",sans-serif;font-weight:700;color:var(--white)}
.poster-text .p1{margin-top:6px;font-size:15px}
.poster-text .p2{font-size:30px;line-height:34px;color:#4fb7e2}
.poster-text .p3{font-size:17px;line-height:22px}
.poster-text .p4{margin-top:6px;font-size:18px}

/* right column */
.promo{left:719px;top:683px;width:211px;height:176px;border:3px solid #d8d8d8;background:linear-gradient(100deg,#1e1e1e 40%,#3a3a3a 100%)}
.promo-photo{left:825px;top:686px;width:102px;height:170px;background:linear-gradient(160deg,#2a2a2a 0%,#5a5a5a 50%,#c26a2a 80%,#2a2a2a 100%)}
.promo-text{left:731px;top:692px;width:190px;font-family:"Roboto Slab",serif;color:#dcdcdc}
.promo-text .w{font-size:16px;line-height:20px}
.promo-text .r{font-weight:700;font-size:28px;color:var(--orange);line-height:30px}
.promo-text .c{font-size:12px;line-height:16px;white-space:nowrap}
.promo-text .n{font-family:"Oswald",sans-serif;font-weight:700;font-size:20px;color:var(--white);line-height:24px;margin:8px 0 0 60px}

.social-widget{left:720px;top:880px;width:209px;height:173px;background:var(--white)}
.social-head{height:24px;background:var(--fb-blue);font-family:"Open Sans",sans-serif;font-weight:700;font-size:15px;color:var(--white);padding-left:8px;line-height:24px}
.social-faces{height:80px;background:linear-gradient(90deg,#d6b8a0,#b88a6e,#e0c4ae,#a37a62,#d8bca6)}
.social-line{margin-top:15px;text-align:center;font-family:"Open Sans",sans-serif;font-weight:600;font-size:14px;color:var(--fb-link)}
.social-btn{position:absolute;left:110px;top:145px;width:81px;height:21px;background:var(--fb-green);border:1px solid #3e7a22;
  text-align:center;line-height:19px;font-family:"Open Sans",sans-serif;font-weight:700;font-size:9px;color:var(--white)}

.footer{left:0;top:1157px;width:1068px;text-align:center;font-size:9px;color:var(--muted)}
</style>
</head>
<body>
<div class="canvas">

  <header>
    <div class="abs brand">
      <div class="brand-mark"></div>
      <div class="brand-name">The Copper Lantern</div>
    </div>
    <div class="abs follow">Follow us on:</div>
    <a class="abs social" style="left:840px" aria-label="Trelvio"></a>
    <a class="abs social" style="left:873px" aria-label="Chirpa"></a>
    <a class="abs social" style="left:906px" aria-label="Linkvo"></a>
    <div class="abs phone-ring">
      <svg width="33" height="33" viewBox="0 0 33 33"><path d="M11 8c-2 1-3 3-2 6 2 5 5 9 10 11 3 1 5 0 6-2l-3-3-3 2c-3-1-5-4-6-7l2-3z" fill="#7a7a7a"/></svg>
    </div>
    <div class="abs phone-number">253 555 0192</div>
  </header>

  <svg class="abs band" width="1068" height="92" viewBox="0 0 1068 92" aria-hidden="true">
    <polygon fill="var(--orange)" points="8,40 60,36 100,30 122,14 160,10 200,5 400,4 600,6 800,3 940,8 948,22 1000,30 1060,34 1066,40 1040,44 1000,50 960,58 948,68 940,86 934,70 900,66 700,62 500,64 300,60 160,64 128,70 122,84 116,68 90,56 50,50 10,46"/>
    <polygon fill="var(--orange-deep)" points="122,50 300,56 500,58 700,56 940,58 940,66 700,62 300,62 122,64"/>
  </svg>

  <nav class="abs nav">
    <a class="current" style="left:170px">Home</a>
    <a style="left:238px">Menus</a>
    <a style="left:304px">Events</a>
    <a style="left:374px">KTB/ PWJ</a>
    <a style="left:440px">Poker</a>
    <a style="left:507px">Karaoke</a>
    <a style="left:597px">Entertainment</a>
    <a style="left:694px">DJ Dancing</a>
    <a style="left:790px">Group Parties</a>
    <a style="left:888px">Contact Us</a>
  </nav>

  <main>
    <div class="abs panel"></div>
    <div class="abs slider-frame"></div>
    <div class="abs slide" role="img" aria-label="Photo of the bar counter with patrons and rows of screens"></div>
    <h1 class="abs headline">Not your Ordinary Sports Bar</h1>
    <div class="abs dots"><span></span><span></span><span></span><span></span><span></span></div>

    <div class="abs leagues">
      <div class="league" style="left:30px"><i style="background:#1f3a8a"></i>VGT</div>
      <div class="league" style="left:182px"><i style="background:#1f3a8a"></i>KTB</div>
      <div class="league" style="left:320px"><i style="background:#d11d25"></i>RVX</div>
      <div class="league" style="left:520px"><i style="background:#d11d25"></i>PWJ</div>
      <div class="league" style="left:680px"><i style="background:#1f3a8a"></i>QDR</div>
    </div>

    <aside class="abs sidebar">
      <div class="tap" style="top:13px"><span>Harlow's</span></div>
      <div class="tap" style="top:102px"><span>Wendler</span></div>
      <div class="tap" style="top:192px"><span>Milo's Cider</span></div>
      <div class="tap" style="top:282px"><span>Maple Light</span></div>
    </aside>

    <h2 class="abs welcome-title">Welcome Message</h2>
    <div class="abs welcome-rule"></div>
    <p class="abs welcome-copy">Lorem ipsum dolor sit amet, consectetur adipiscing elit. Morbi condimentum vestibulum tortor, rhoncus cursus justo porta ut. Donec nec nunc mauris, vitae laoreet mi. Aenean in massa quis quam consectetur fermentum. Pellentesque vulputate lorem sapien. Proin vel mi interdum sem facilisis scelerisque. Nullam sit amet dui a nunc sagittis commodo a quis lectus. Morbi vestibulum bibendum viverra. Donec feugiat ullamcorper velit sit amet vulputate. Sed eget urna lectus. Fusce ac leo velit.</p>

    <div class="abs feature"></div>
    <h3 class="abs feature-title">View This @ The Copper Lantern</h3>
    <div class="abs poster" role="img" aria-label="Fight night poster with four fighters"></div>
    <div class="abs poster-text">
      <div class="p1">TWO TITLE FIGHTS</div>
      <div class="p2">PWJ 136</div>
      <div class="p3">DORSEY vs MALDEN</div>
      <div class="p3">ALTON vs FENWICK</div>
      <div class="p4">SATURDAY OCT. 8 · ORRIN CENTER</div>
    </div>

    <div class="abs promo"></div>
    <div class="abs promo-photo" role="img" aria-label="Rugby player holding a ball"></div>
    <div class="abs promo-text">
      <div class="w">Watch</div>
      <div class="r">RUGBY</div>
      <div class="c">Tri-Oceans Cup here @</div>
      <div class="n">The Copper<br>Lantern</div>
    </div>

    <div class="abs social-widget">
      <div class="social-head">Trelvio</div>
      <div class="social-faces" role="img" aria-label="Grid of member profile photos"></div>
      <div class="social-line">Find &amp; connect with friends</div>
      <div class="social-btn">Sign Up</div>
    </div>
  </main>

  <footer class="abs footer">The Copper Lantern, Copyright © 2012</footer>
</div>
</body>
</html>
```